Job Coaching - Moval; engaging people to improve their work experience

I need a flyer for Job Coaching. It serves to engage customers (not businesses) with problems in their daily job, typical questions that are handled are:
Do I fit for the job?
Am I using my talents at best in this job?
I have a conflict with my manager/colleagues, what should I do?
My work-life balance is a mess, how can I improve this?
What job fits best with my talents?
I'm getting stressed out from my job, what can I do?
....
This Flyer will be available at GP's, therpeutic practices, pharamcists,...
this flyer should put people in action to contact me
Flyer can be created in English, in the final one the text should be in Dutch; I will make the translation of the selected flyer and provide it at the end

Target Market(s)

consumers / customers / people having a job, but somewhat stuck in it

Industry/Entity Type

Professional Coaching

Requirements
Must have
• the questions mentioned in the project description; mobile number: 0472/318946; email: tom.verlinde@movalcoaching.example; website: www.movalcoaching.example ; it should make also reference to 'Career guidance cheques of the GBRO'

```html
<!DOCTYPE html>
<html lang="en">
<head>
<meta charset="utf-8">
<title>Moval – Career Guidance Flyer</title>
<link href="https://fonts.googleapis.com/css2?family=Montserrat:wght@400;500;600;700;800&display=swap" rel="stylesheet">
<style>
  :root{
    --teal:#2fa89f;
    --teal-soft:#8fd0c9;
    --grey:#666769;
    --grey-dark:#555658;
    --ink:#3a3a3c;
    --paper:#ffffff;
    --backdrop:#ecebe8;
  }
  *{box-sizing:border-box;margin:0;padding:0}
  html,body{width:1200px;height:1200px;overflow:hidden;background:var(--backdrop);font-family:'Montserrat',sans-serif}
  .flyer{position:absolute;left:195px;top:30px;width:810px;height:1140px;background:var(--paper);overflow:hidden;box-shadow:0 2px 10px rgba(0,0,0,.12)}
  .abs{position:absolute}

  .hero-photo{left:300px;top:0;width:510px;height:380px;
    background:linear-gradient(180deg,rgba(102,103,105,0) 70%,var(--grey) 100%),
      linear-gradient(90deg,#fff 0%,rgba(255,255,255,0) 30%),
      linear-gradient(135deg,#c9d3dc 0%,#a9b6c3 40%,#8c98a6 70%,#7b8591 100%)}

  .brand{left:32px;top:58px;display:flex;align-items:center;gap:14px}
  .brand-dot{width:76px;height:76px;border-radius:50%;background:var(--teal)}
  .brand-text{display:flex;flex-direction:column}
  .brand-name{font-weight:700;font-size:58px;line-height:1;color:var(--teal);letter-spacing:1px}
  .brand-tag{font-weight:500;font-size:15px;color:var(--grey);margin-top:2px}

  .title{left:42px;top:168px;font-weight:800;font-size:64px;line-height:62px;letter-spacing:.5px}
  .title .t1{color:var(--teal)}
  .title .t2{color:var(--grey-dark)}
  .title-pill{left:45px;top:287px;height:34px;padding:0 16px;border-radius:10px;background:var(--teal);color:#fff;font-size:24px;font-weight:500;line-height:34px;letter-spacing:.5px;box-shadow:2px 2px 0 #fff,3px 3px 0 var(--grey)}

  .band{left:0;top:0;width:810px;height:1140px}

  .portrait{left:5px;top:400px;width:250px;height:250px;border-radius:50%;
    background:radial-gradient(circle at 50% 40%,#b5897a 0%,#8a3a3e 45%,#5b2027 100%);border:6px solid #fff}

  .intro{left:300px;top:375px;width:468px;color:#fff;text-align:right;font-size:13px;line-height:17px}
  .intro p{margin-bottom:16px}
  .intro .lead{font-weight:700}

  .ask{left:149px;top:690px;width:534px;height:58px;border:2px solid var(--grey);background:#fff;box-shadow:-10px 12px 0 var(--grey);display:flex;align-items:center;justify-content:center;text-align:center;color:var(--teal);font-weight:700;font-size:19px;line-height:22px;letter-spacing:.3px}

  .questions{left:62px;top:778px;width:720px;display:grid;grid-template-columns:372px 348px;row-gap:12px;list-style:none}
  .q{display:flex;align-items:center;gap:14px;height:66px}
  .q-icon{flex:0 0 64px;width:64px;height:64px;border-radius:50%;background:var(--teal);border:5px solid var(--teal-soft);display:flex;align-items:center;justify-content:center}
  .q-text{color:var(--ink);font-size:16px;line-height:20px;max-width:270px}

  .note{left:149px;top:1010px;width:534px;height:24px;border-radius:12px;background:var(--grey);color:#fff;font-size:12.5px;font-weight:700;line-height:24px;text-align:center}

  .phone{left:55px;top:1055px;width:270px;height:54px;border:3px solid var(--teal);border-radius:10px;background:#fff;display:flex;align-items:center;gap:10px;padding-left:14px;color:var(--grey-dark);font-weight:700;font-size:29px}
  .site{left:400px;top:1048px;width:410px;height:42px;color:#fff;font-size:25px;font-weight:500;line-height:42px;text-align:center;letter-spacing:.3px}
  .mail{left:390px;top:1090px;width:420px;height:40px;color:#fff;font-size:15px;font-weight:600;line-height:40px;text-align:center}
</style>
</head>
<body>
<main class="flyer">
  <div class="abs hero-photo" role="img" aria-label="Photo of a coach presenting to a seated group in a workshop"></div>

  <svg class="abs band" viewBox="0 0 810 1140" aria-hidden="true">
    <path d="M0 370 L810 370 L810 650 C640 632 470 640 300 680 C200 703 110 710 0 705 Z" fill="var(--grey)"/>
    <path d="M300 680 C470 630 640 620 810 650 L810 695 C650 650 470 650 300 680 Z" fill="var(--teal)"/>
    <path d="M300 680 C470 640 650 625 810 645" fill="none" stroke="#fff" stroke-width="4"/>
    <path d="M70 650 L60 755 L120 660 Z" fill="var(--grey)"/>
  </svg>

  <div class="brand abs">
    <span class="brand-dot"></span>
    <div class="brand-text">
      <span class="brand-name">Moval</span>
      <span class="brand-tag">professional coaching</span>
    </div>
  </div>

  <h1 class="title abs"><span class="t1">CAREER</span><br><span class="t2">GUIDANCE</span></h1>
  <div class="title-pill abs">WITH CAREER VOUCHERS</div>

  <div class="portrait abs" role="img" aria-label="Portrait photo of the coach in a red shirt"></div>

  <div class="intro abs">
    <p>We easily spend 8 hours a day on our professional pursuits, our job. If we assume that we sleep about 8 hours a day, that's 50% of our active time. We actually spend more time with our colleagues than with our partner and/or children.</p>
    <p>In addition, if things are not going well during those 8 hours, it also impacts the other 8 waking hours. If we don't feel good about ourselves at work, our family members, friends &amp; acquaintances feel it too.</p>
    <p>So we'd better make sure that we spend those 8 hours meaningfully &amp;, at best, get energy from it too. That we can accomplish a piece of our personal accomplishments there.</p>
    <p class="lead">During this career counseling, we take a close look at your personal situation.</p>
  </div>

  <h2 class="ask abs">DO YOU RECOGNIZE YOURSELF IN ANY OF THE<br>FOLLOWING QUESTIONS?</h2>

  <ul class="questions abs">
    <li class="q">
      <span class="q-icon"><svg width="30" height="30" viewBox="0 0 24 24"><path d="M14 2 L5 14 H11 L9 22 L19 9 H13 Z" fill="#fff"/></svg></span>
      <span class="q-text">How can I get more energy from my job?</span>
    </li>
    <li class="q">
      <span class="q-icon"><svg width="32" height="32" viewBox="0 0 24 24" fill="none" stroke="#fff" stroke-width="1.8" stroke-linecap="round"><path d="M6 9 L12 5 L18 9"/><path d="M12 19 V13 M9 20 V15 M15 20 V15"/><path d="M4 19 H20"/></svg></span>
      <span class="q-text">How can I get a better work-life balance?</span>
    </li>
    <li class="q">
      <span class="q-icon"><svg width="32" height="32" viewBox="0 0 24 24" fill="#fff"><path d="M12 2 l1.2 2.6 2.8.3-2.1 1.9.6 2.8L12 8.2 9.5 9.6l.6-2.8L8 4.9l2.8-.3z"/><circle cx="12" cy="14" r="2.6"/><path d="M7 22 c0-3 2.2-5 5-5 s5 2 5 5z"/></svg></span>
      <span class="q-text">What are my talents?</span>
    </li>
    <li class="q">
      <span class="q-icon"><svg width="32" height="32" viewBox="0 0 24 24" fill="none" stroke="#fff" stroke-width="1.8" stroke-linejoin="round"><rect x="3" y="8" width="18" height="12" rx="2"/><path d="M9 8 V5 H15 V8"/><path d="M3 13 H21"/></svg></span>
      <span class="q-text">How can I work better with my manager and/or colleagues?</span>
    </li>
    <li class="q">
      <span class="q-icon"><svg width="32" height="32" viewBox="0 0 24 24" fill="#fff"><ellipse cx="8" cy="8" rx="3" ry="4.5"/><ellipse cx="8" cy="16.5" rx="2.4" ry="2"/><ellipse cx="16" cy="6" rx="3" ry="4.5"/><ellipse cx="16" cy="14.5" rx="2.4" ry="2"/></svg></span>
      <span class="q-text">Do you know what you want, but do not dare to take the step?</span>
    </li>
    <li class="q">
      <span class="q-icon"><svg width="30" height="30" viewBox="0 0 24 24" fill="none" stroke="#fff" stroke-width="2" stroke-linecap="round" stroke-linejoin="round"><rect x="3" y="5" width="18" height="16" rx="2"/><path d="M3 10 H21 M8 3 V7 M16 3 V7"/><path d="M8.5 15 L11 17.5 L15.5 13"/></svg></span>
      <span class="q-text">Maybe you think you have more up your sleeve than you do today?</span>
    </li>
  </ul>

  <p class="note abs">Then we will work on this together.&nbsp; GBRO career cheques, these can be used.</p>

  <svg class="abs" style="left:0;top:0" width="810" height="1140" viewBox="0 0 810 1140" aria-hidden="true">
    <path d="M395 1048 H810 V1090 H380 Z" fill="var(--grey)"/>
    <path d="M380 1090 H810 V1130 H365 Z" fill="var(--teal)"/>
    <path d="M380 1048 L395 1048 L365 1130 L352 1130 Z" fill="var(--grey)"/>
  </svg>

  <div class="phone abs">
    <svg width="24" height="24" viewBox="0 0 24 24"><path d="M6.6 10.8a15.1 15.1 0 0 0 6.6 6.6l2.2-2.2a1 1 0 0 1 1-.25 11.4 11.4 0 0 0 3.6.57 1 1 0 0 1 1 1V20a1 1 0 0 1-1 1A17 17 0 0 1 3 4a1 1 0 0 1 1-1h3.5a1 1 0 0 1 1 1c0 1.25.2 2.45.57 3.57a1 1 0 0 1-.25 1z" fill="var(--grey-dark)"/></svg>
    <span>0472/318946</span>
  </div>
  <div class="site abs">www.movalcoaching.example</div>
  <div class="mail abs">tom.verlinde@movalcoaching.example</div>
</main>
</body>
</html>
```